Real Estate "For Sale" Sign for construction company

We need a sign that we can use to hang on a post and place on the road when we sell a property. The sign will be simple and will need to mainly feature our logo (files attached), as well as the words "For Sale", and then our phone number "(555) 617 3489". The sign will hang on a post that'll look something like the attached picture.

Target Market(s)

Home buyers

Industry/Entity Type

Real Estate

Font styles to use
Serif
Sans Serif

Colors
0054AA
0677BA
7BADD7
CADEEF
E8F1F8
0094D4
00A9DD
6FCCEA
C7EBF8
E9F6FB

Requirements
Must have
• For Sale & our phone number

```html
<!DOCTYPE html>
<html lang="en">
<head>
<meta charset="utf-8">
<title>For Sale Sign – Ridgecrest Oak Realty</title>
<link href="https://fonts.googleapis.com/css2?family=Montserrat:wght@500;800;900&family=Bebas+Neue&display=swap" rel="stylesheet">
<style>
  :root {
    --deep-blue: #0054AA;
    --mid-blue: #0677BA;
    --bright-blue: #0094D4;
    --sky-blue: #00A9DD;
    --light-cyan: #3CC3EF;
    --pale-band: #8ED8F8;
    --navy: #12285C;
    --white: #ffffff;
    --page-bg: #eef3f8;
  }
  * { margin: 0; padding: 0; box-sizing: border-box; }
  html, body {
    width: 1200px;
    height: 1200px;
    overflow: hidden;
    background: var(--page-bg);
  }
  .sign {
    position: absolute;
    left: 172px;
    top: 40px;
    width: 856px;
    height: 1120px;
    background: var(--white);
    overflow: hidden;
    box-shadow: 0 6px 24px rgba(18, 40, 92, 0.18);
  }
  .headline-panel {
    position: absolute;
    left: 0; top: 0;
    width: 100%;
    height: 470px;
    overflow: hidden;
    background: linear-gradient(110deg, var(--deep-blue) 0%, var(--mid-blue) 40%, var(--bright-blue) 70%, var(--light-cyan) 100%);
  }
  .headline {
    position: absolute;
    left: 0; width: 100%;
    text-align: center;
    font-family: "Montserrat", sans-serif;
    font-weight: 900;
    color: var(--white);
    font-size: 250px;
    line-height: 1;
    letter-spacing: -0.01em;
  }
  .headline--for { top: 44px; }
  .headline--sale { top: 254px; font-size: 262px; }

  .brand {
    position: absolute;
    left: 0; top: 520px;
    width: 100%;
    text-align: center;
  }
  .brand__mark {
    width: 176px;
    height: 176px;
    margin: 0 auto 18px;
    border-radius: 50%;
    background: var(--mid-blue);
  }
  .brand__name {
    font-family: "Montserrat", sans-serif;
    font-weight: 500;
    font-size: 60px;
    line-height: 1;
    color: var(--mid-blue);
    letter-spacing: -0.01em;
  }
  .brand__tagline {
    margin-top: 16px;
    font-family: "Montserrat", sans-serif;
    font-weight: 500;
    font-size: 19px;
    letter-spacing: 0.6em;
    padding-left: 0.6em;
    color: var(--mid-blue);
  }

  .contact-band {
    position: absolute;
    left: 0; top: 858px;
    width: 100%;
    height: 156px;
    background: linear-gradient(90deg, var(--navy) 0%, var(--deep-blue) 50%, var(--navy) 100%);
    display: flex;
    align-items: center;
    padding-left: 70px;
    gap: 22px;
  }
  .contact-band__icon { width: 94px; height: 94px; flex: none; }
  .contact-band__phone {
    font-family: "Bebas Neue", sans-serif;
    font-size: 124px;
    line-height: 1;
    color: var(--white);
    letter-spacing: 0.02em;
    padding-top: 10px;
    text-shadow: 2px 3px 4px rgba(0, 0, 0, 0.35);
  }
  .footer-band {
    position: absolute;
    left: 0; top: 1032px;
    width: 100%;
    height: 88px;
    background: var(--pale-band);
  }
</style>
</head>
<body>
  <main class="sign">
    <section class="headline-panel">
      <div class="headline headline--for">FOR</div>
      <div class="headline headline--sale">SALE</div>
    </section>

    <section class="brand">
      <div class="brand__mark"></div>
      <div class="brand__name">Ridgecrest Oak</div>
      <div class="brand__tagline">REALTY</div>
    </section>

    <section class="contact-band">
      <svg class="contact-band__icon" viewBox="0 0 100 100" aria-hidden="true">
        <circle cx="50" cy="50" r="48" fill="#ffffff"/>
        <path d="M36 26c2-1 4 0 5 2l5 10c1 2 0 4-1 5l-4 3c2 6 7 11 13 14l3-4c1-2 3-2 5-1l10 5c2 1 3 3 2 5l-2 6c-1 3-4 5-7 4C45 72 30 57 27 38c-1-3 1-6 4-7z" fill="#12285C"/>
        <path d="M58 28a16 16 0 0 1 15 15M58 20a24 24 0 0 1 23 23" stroke="#12285C" stroke-width="4" fill="none" stroke-linecap="round"/>
      </svg>
      <div class="contact-band__phone">(555) 617 3489</div>
    </section>

    <div class="footer-band"></div>
  </main>
</body>
</html>
```